Bright Path Therapies business cards and stationary

Need business cards and stationary designed to match previously made logo for for a new company based in Sydney NSW called 'Bright Path Therapies'.

We provide early intervention services and diagnostic assessment for children with disability and their families. I would like designs that are colourful and child friendly - possibly using feet/footprints/steps on a white background. The final design should communicate that we are family friendly, accepting and fun to work with.

Target Market(s)

Parents and Families
Teachers
Allied Health Professionals

Industry/Entity Type

Psychology

Contact Information for Business Card

Bright Path Therapies
www.brightpaththerapies.example
info@brightpaththerapies.example

Font styles to use
Sans Serif
Decorative
Script

Requirements
Must have
• Match the font and colour scheme of logo, along with footprint picture
Nice to have
• Clean and simple, while reflecting that I am working with families.
• Also- editable for when we make staff specific cards.

```html
<!DOCTYPE html>
<html lang="en">
<head>
<meta charset="utf-8">
<title>Bright Path Therapies – Business Cards</title>
<link rel="stylesheet" href="https://fonts.googleapis.com/css2?family=Patrick+Hand&family=Open+Sans:wght@400;600&display=swap">
<style>
  :root {
    --backdrop: #e3e4e7;
    --paper: #ffffff;
    --red: #f2292b;
    --blue: #2f7ad8;
    --orange: #f7a21f;
    --green: #7cc53a;
    --ink-light: #ffffff;
  }
  * { box-sizing: border-box; margin: 0; padding: 0; }
  html, body {
    width: 1200px; height: 1200px; overflow: hidden;
    background: var(--backdrop);
  }
  .sheet {
    width: 1200px; height: 1200px;
    display: flex; flex-direction: column; align-items: center; justify-content: center;
    gap: 56px;
  }
  .card {
    position: relative;
    width: 900px; height: 514px;
    background: var(--paper);
    overflow: hidden;
    box-shadow: 0 6px 18px rgba(0,0,0,0.12);
  }

  /* Brand name block (stands in for the mark) */
  .brand {
    position: absolute;
    display: flex; align-items: center; gap: 18px;
  }
  .brand-dot {
    width: 74px; height: 74px; border-radius: 50%;
    background: var(--red);
  }
  .brand-name {
    font-family: "Patrick Hand", cursive;
    color: var(--blue);
    font-size: 64px; line-height: 1;
    letter-spacing: 1px;
  }

  /* Back of card */
  .card-back .stripes { position: absolute; }
  .card-back .stripes-top { left: 40px; top: 36px; }
  .card-back .stripes-bottom { right: 36px; bottom: 150px; }
  .card-back .brand { left: 220px; top: 110px; }
  .tagline {
    position: absolute; left: 0; right: 0; top: 215px;
    text-align: center;
    font-family: "Patrick Hand", cursive;
    font-size: 56px; line-height: 1;
  }
  .tagline .w1 { color: var(--red); }
  .tagline .w2 { color: var(--blue); }
  .tagline .w3 { color: var(--orange); }
  .tagline .w4 { color: var(--green); }
  .contact-bands { position: absolute; left: 0; bottom: 0; width: 900px; height: 150px; }
  .contact-row {
    position: absolute; left: 0; right: 0; bottom: 40px; height: 62px;
    display: flex; align-items: center; justify-content: center; gap: 26px;
    font-family: "Open Sans", sans-serif; font-size: 21px; color: var(--ink-light);
  }
  .contact-item { display: flex; align-items: center; gap: 12px; }
  .contact-divider { width: 2px; height: 30px; background: var(--ink-light); transform: skewX(-20deg); }

  /* Front of card */
  .footprint-field {
    position: absolute; inset: 0;
    background:
      radial-gradient(circle at 12% 25%, rgba(47,122,216,0.12), transparent 22%),
      radial-gradient(circle at 20% 70%, rgba(242,41,43,0.10), transparent 20%),
      radial-gradient(circle at 38% 88%, rgba(247,162,31,0.12), transparent 20%),
      radial-gradient(circle at 70% 85%, rgba(124,197,58,0.10), transparent 22%),
      radial-gradient(circle at 88% 70%, rgba(247,162,31,0.10), transparent 20%),
      radial-gradient(circle at 30% 10%, rgba(242,41,43,0.08), transparent 18%);
  }
  .card-front .brand { left: 200px; top: 215px; }
  .card-front .brand-dot { width: 96px; height: 96px; }
  .card-front .brand-name { font-size: 76px; }
  .web-pill {
    position: absolute; right: -20px; top: 34px;
    background: var(--red); color: var(--ink-light);
    font-family: "Open Sans", sans-serif; font-size: 20px;
    padding: 10px 44px 10px 26px; border-radius: 24px;
  }
  .front-edge { position: absolute; left: 0; bottom: 0; width: 900px; height: 14px; display: flex; }
  .front-edge span { flex: 1; }
</style>
</head>
<body>
<main class="sheet">

  <!-- Card back: contact side -->
  <section class="card card-back">
    <svg class="stripes stripes-top" width="130" height="110" viewBox="0 0 130 110" aria-hidden="true">
      <rect x="40" y="0" width="90" height="14" rx="7" fill="var(--red)"/>
      <rect x="26" y="28" width="90" height="14" rx="7" fill="var(--blue)"/>
      <rect x="12" y="56" width="90" height="14" rx="7" fill="var(--orange)"/>
      <rect x="0" y="84" width="90" height="14" rx="7" fill="var(--green)"/>
    </svg>

    <div class="brand">
      <span class="brand-dot"></span>
      <span class="brand-name">Bright Path Therapies</span>
    </div>

    <p class="tagline">
      <span class="w1">Bright</span> <span class="w2">Path</span> <span class="w3">Therapies</span>
    </p>

    <svg class="stripes stripes-bottom" width="130" height="110" viewBox="0 0 130 110" aria-hidden="true">
      <rect x="40" y="0" width="90" height="14" rx="7" fill="var(--red)"/>
      <rect x="26" y="28" width="90" height="14" rx="7" fill="var(--blue)"/>
      <rect x="12" y="56" width="90" height="14" rx="7" fill="var(--orange)"/>
      <rect x="0" y="84" width="90" height="14" rx="7" fill="var(--green)"/>
    </svg>

    <svg class="contact-bands" viewBox="0 0 900 150" preserveAspectRatio="none" aria-hidden="true">
      <polygon points="0,118 430,118 460,134 900,134 900,150 0,150" fill="var(--blue)"/>
      <rect x="0" y="48" width="900" height="62" fill="var(--red)"/>
    </svg>
    <div class="contact-row">
      <span class="contact-item">
        <svg width="30" height="30" viewBox="0 0 30 30" aria-hidden="true">
          <circle cx="15" cy="15" r="14" fill="none" stroke="#fff" stroke-width="2"/>
          <rect x="8" y="10" width="14" height="10" fill="none" stroke="#fff" stroke-width="1.6"/>
          <polyline points="8,10 15,16 22,10" fill="none" stroke="#fff" stroke-width="1.6"/>
        </svg>
        info@brightpaththerapies.example
      </span>
      <span class="contact-divider"></span>
      <span class="contact-item">
        <svg width="30" height="30" viewBox="0 0 30 30" aria-hidden="true">
          <circle cx="15" cy="15" r="14" fill="none" stroke="#fff" stroke-width="2"/>
          <circle cx="15" cy="15" r="8" fill="none" stroke="#fff" stroke-width="1.6"/>
          <ellipse cx="15" cy="15" rx="3.5" ry="8" fill="none" stroke="#fff" stroke-width="1.4"/>
          <line x1="7" y1="15" x2="23" y2="15" stroke="#fff" stroke-width="1.4"/>
        </svg>
        www.brightpaththerapies.example
      </span>
    </div>
  </section>

  <!-- Card front: brand side -->
  <section class="card card-front">
    <div class="footprint-field" role="img" aria-label="Faint scattered pastel footprints in blue, red, orange and green across the card"></div>
    <div class="web-pill">www.brightpaththerapies.example</div>
    <div class="brand">
      <span class="brand-dot"></span>
      <span class="brand-name">Bright Path Therapies</span>
    </div>
    <div class="front-edge" aria-hidden="true">
      <span style="background:var(--red)"></span>
      <span style="background:var(--blue)"></span>
      <span style="background:var(--orange)"></span>
      <span style="background:var(--green)"></span>
    </div>
  </section>

</main>
</body>
</html>
```